Business Card Design

New company looking for logo, for business cards and email signature.
we provide Safety, Training and Project Management Services to Mining and Transport sectors.

Industry/Entity Type

Business

Contact Information for Business Card

HOLLOWAY CONSULTANCY, Tom Westcott, Principal Consultant, 0491362284, hollowayconsultancy@examplemail.test , Unit 214,Kestrel Point Trade Centre,581 Tamsin Street, Brackenfield, 5821.
DEPENDABLE OPERATIONS DRIVEN BY SAFETY, COACHING AND GUIDANCE.

```html
<!DOCTYPE html>
<html lang="en">
<head>
<meta charset="utf-8">
<title>Holloway Consultancy – Business Cards</title>
<link rel="stylesheet" href="https://fonts.googleapis.com/css2?family=Arimo:wght@400;700&family=Oswald:wght@400;500&display=swap">
<style>
  :root {
    --page: #f4f4f4;
    --card-top: #1d1f21;
    --card-bottom: #050505;
    --orange: #e07a24;
    --silver: #d4d6d8;
    --white: #f2f2f2;
    --rule: #9a9c9e;
    --divider: #6c6e70;
  }
  * { margin: 0; padding: 0; box-sizing: border-box; }
  html, body { width: 1200px; height: 900px; overflow: hidden; }
  body {
    background: var(--page);
    font-family: "Arimo", Arial, sans-serif;
    position: relative;
  }
  .card {
    position: absolute;
    top: 295px;
    width: 540px;
    height: 310px;
    border-radius: 24px;
    background: radial-gradient(ellipse at 45% 25%, var(--card-top) 0%, #0e0f10 55%, var(--card-bottom) 100%);
    box-shadow: 0 18px 30px rgba(0,0,0,0.25);
    overflow: hidden;
    color: var(--white);
  }
  .card--front { left: 40px; }
  .card--back { left: 620px; }

  .wordmark {
    display: flex;
    align-items: center;
    gap: 12px;
    font-family: "Oswald", "Arial Narrow", sans-serif;
    font-weight: 500;
    color: var(--silver);
    letter-spacing: 3px;
    white-space: nowrap;
  }
  .wordmark__square {
    width: 34px; height: 34px;
    background: var(--orange);
    flex: none;
  }
  .card--front .wordmark {
    position: absolute;
    left: 0; right: 0;
    top: 118px;
    justify-content: center;
    font-size: 30px;
  }
  .tagline {
    position: absolute;
    left: 22px; right: 22px;
    bottom: 22px;
    font-family: "Oswald", "Arial Narrow", sans-serif;
    font-size: 12.5px;
    letter-spacing: 1.6px;
    color: var(--orange);
    white-space: nowrap;
  }

  .card--back .wordmark {
    position: absolute;
    left: 0; right: 0;
    top: 96px;
    justify-content: center;
    font-size: 27px;
  }
  .back-rule {
    position: absolute;
    left: 0; right: 0;
    top: 176px;
    height: 3px;
    background: linear-gradient(90deg, #555 0%, var(--rule) 50%, #d8d8d8 100%);
  }
  .person {
    position: absolute;
    right: 290px;
    top: 212px;
    text-align: right;
  }
  .person__name {
    font-size: 19px;
    color: var(--orange);
    line-height: 1.2;
  }
  .person__role {
    font-size: 13px;
    color: var(--white);
    margin-top: 2px;
  }
  .divider {
    position: absolute;
    left: 266px;
    top: 190px;
    width: 1px;
    height: 100px;
    background: var(--divider);
  }
  .contact {
    position: absolute;
    left: 280px;
    top: 196px;
    list-style: none;
    font-size: 11.5px;
    line-height: 15px;
    color: var(--white);
  }
  .contact__item { display: flex; gap: 6px; }
  .contact__icon { width: 12px; height: 12px; flex: none; margin-top: 2px; fill: var(--orange); }
</style>
</head>
<body>
  <section class="card card--front" aria-label="Business card front">
    <div class="wordmark"><span class="wordmark__square"></span>HOLLOWAY CONSULTANCY</div>
    <p class="tagline">DEPENDABLE OPERATIONS DRIVEN BY SAFETY, COACHING AND GUIDANCE</p>
  </section>

  <section class="card card--back" aria-label="Business card back">
    <div class="wordmark"><span class="wordmark__square"></span>HOLLOWAY CONSULTANCY</div>
    <div class="back-rule"></div>
    <div class="person">
      <p class="person__name">Tom Westcott</p>
      <p class="person__role">Principal Consultant</p>
    </div>
    <div class="divider"></div>
    <ul class="contact">
      <li class="contact__item">
        <svg class="contact__icon" viewBox="0 0 24 24" aria-hidden="true"><path d="M6.6 10.8a15.1 15.1 0 0 0 6.6 6.6l2.2-2.2c.3-.3.7-.4 1-.2 1.1.4 2.3.6 3.6.6.6 0 1 .4 1 1V20c0 .6-.4 1-1 1A17 17 0 0 1 3 4c0-.6.4-1 1-1h3.5c.6 0 1 .4 1 1 0 1.3.2 2.5.6 3.6.1.3 0 .7-.2 1z"/></svg>
        <span>0491362284</span>
      </li>
      <li class="contact__item">
        <svg class="contact__icon" viewBox="0 0 24 24" aria-hidden="true"><path d="M2 5h20v14H2z M4 7v.5l8 5 8-5V7l-8 5z" fill-rule="evenodd"/></svg>
        <span>hollowayconsultancy@examplemail.test</span>
      </li>
      <li class="contact__item">
        <svg class="contact__icon" viewBox="0 0 24 24" aria-hidden="true"><path d="M12 3 2 12h3v9h5v-6h4v6h5v-9h3z"/></svg>
        <span>Unit 214,Kestrel Point<br>Trade Centre,581 Tamsin Street<br>Brackenfield, 5821</span>
      </li>
    </ul>
  </section>
</body>
</html>
```